business card stylish and chique

I'd like to have a new business card. I am a certified pilates instructor. my website is www.brightcoremotion.example. Next to teaching pilates in napa valley and around the globe, I offer luxury wellness travel in Napa Valley. (plus I make art and healthy food. my instagram is @lra_vmbk)
I'd love to have an eye catching (bold and unique) card that says in gold or embossed LRA VMBK . (but open for any creative idea)
The back should have my info:
LorraVambeck@mailbox.example.
I love whimsical and think the murals at the Orlis hotel in Miami and the Tavro prints are my dreamworld. I'd love on the back my email address and the whimsical design.

Target Market(s)

see description

Industry/Entity Type

Health And Wellness

Contact Information for Business Card

see above

Colors

Designer to choose colors to be used in the design.

Requirements
Must have
• multicolor on back, whimsical print (allowed to use, pref own design)
• probably just white (or black or other single color with LRA VMBK standing out
Nice to have
• open
Should not have
• crazy fonts

```html
<!DOCTYPE html>
<html lang="en">
<head>
<meta charset="utf-8">
<title>Lorra Vambeck – Business Card</title>
<link href="https://fonts.googleapis.com/css2?family=Oswald:wght@300;500&family=Open+Sans:wght@400&display=swap" rel="stylesheet">
<style>
  :root {
    --stage: #e9e8e6;
    --card-black: #161616;
    --emboss-face: #121212;
    --emboss-light: rgba(255,255,255,0.14);
    --emboss-dark: rgba(0,0,0,0.9);
    --gold: #b8913f;
    --ink: #2a2a2a;
    --tint-blue: #d4e8f3;
    --tint-green: #dcebd2;
    --tint-sand: #ebe1cf;
    --paper: #f6f5f0;
  }
  * { margin: 0; padding: 0; box-sizing: border-box; }
  html, body {
    width: 1200px; height: 900px; overflow: hidden;
    background: var(--stage);
  }
  .canvas {
    position: relative; width: 1200px; height: 900px;
    display: flex; flex-direction: column; align-items: center; justify-content: center; gap: 40px;
  }
  .card {
    position: relative; width: 700px; height: 400px;
    box-shadow: 0 6px 18px rgba(0,0,0,0.18);
    overflow: hidden;
  }
  .card-front { background: var(--card-black); display: flex; align-items: center; justify-content: center; }
  .monogram {
    font-family: 'Oswald', sans-serif; font-weight: 300;
    font-size: 80px; letter-spacing: 2px;
    color: var(--emboss-face);
    text-shadow: -1px -1px 0 var(--emboss-dark), 1px 1px 0 var(--emboss-light), 2px 3px 4px rgba(0,0,0,0.6);
    transform: translateY(-24px);
  }
  .card-back { background: var(--paper); }
  .print-area { position: absolute; inset: 0; width: 700px; height: 400px; }
  .tile-blue { fill: var(--tint-blue); }
  .tile-green { fill: var(--tint-green); }
  .tile-sand { fill: var(--tint-sand); }
  .tile-grid rect { stroke: var(--paper); stroke-width: 3; }
  .veil { fill: var(--paper); opacity: 0.25; }
  .identity {
    position: absolute; left: 0; right: 0; top: 164px;
    display: flex; align-items: center;
  }
  .name {
    width: 340px; text-align: right; padding-right: 14px;
    font-family: 'Oswald', sans-serif; font-weight: 500;
    font-size: 31px; color: var(--gold); text-transform: uppercase; letter-spacing: 0.3px;
  }
  .divider { width: 1.5px; height: 70px; background: var(--ink); }
  .contacts { list-style: none; padding-left: 11px; }
  .contact {
    display: flex; align-items: center; gap: 8px;
    font-family: 'Open Sans', sans-serif; font-size: 13.5px; color: var(--ink); line-height: 22px;
  }
  .contact svg { width: 12px; height: 12px; flex: none; }
</style>
</head>
<body>
<main class="canvas">
  <section class="card card-front" aria-label="Card front">
    <h1 class="monogram">LRA VMBK</h1>
  </section>

  <section class="card card-back" aria-label="Card back">
    <svg class="print-area" viewBox="0 0 700 400" role="img" aria-label="Whimsical multicolour tiled print in pale blue, green and sand">
      <g class="tile-grid">
        <rect class="tile-blue" x="0" y="0" width="78" height="80"/>
        <rect class="tile-sand" x="78" y="0" width="78" height="80"/>
        <rect class="tile-green" x="156" y="0" width="78" height="80"/>
        <rect class="tile-sand" x="234" y="0" width="78" height="80"/>
        <rect class="tile-green" x="312" y="0" width="78" height="80"/>
        <rect class="tile-blue" x="390" y="0" width="78" height="80"/>
        <rect class="tile-sand" x="468" y="0" width="78" height="80"/>
        <rect class="tile-green" x="546" y="0" width="78" height="80"/>
        <rect class="tile-blue" x="624" y="0" width="78" height="80"/>

        <rect class="tile-sand" x="0" y="80" width="78" height="80"/>
        <rect class="tile-green" x="78" y="80" width="78" height="80"/>
        <rect class="tile-blue" x="156" y="80" width="78" height="80"/>
        <rect class="tile-green" x="234" y="80" width="78" height="80"/>
        <rect class="tile-sand" x="312" y="80" width="78" height="80"/>
        <rect class="tile-green" x="390" y="80" width="78" height="80"/>
        <rect class="tile-blue" x="468" y="80" width="78" height="80"/>
        <rect class="tile-sand" x="546" y="80" width="78" height="80"/>
        <rect class="tile-green" x="624" y="80" width="78" height="80"/>

        <rect class="tile-green" x="0" y="160" width="78" height="80"/>
        <rect class="tile-blue" x="78" y="160" width="78" height="80"/>
        <rect class="tile-sand" x="156" y="160" width="78" height="80"/>
        <rect class="tile-blue" x="234" y="160" width="78" height="80"/>
        <rect class="tile-green" x="312" y="160" width="78" height="80"/>
        <rect class="tile-sand" x="390" y="160" width="78" height="80"/>
        <rect class="tile-green" x="468" y="160" width="78" height="80"/>
        <rect class="tile-blue" x="546" y="160" width="78" height="80"/>
        <rect class="tile-sand" x="624" y="160" width="78" height="80"/>

        <rect class="tile-blue" x="0" y="240" width="78" height="80"/>
        <rect class="tile-green" x="78" y="240" width="78" height="80"/>
        <rect class="tile-sand" x="156" y="240" width="78" height="80"/>
        <rect class="tile-green" x="234" y="240" width="78" height="80"/>
        <rect class="tile-blue" x="312" y="240" width="78" height="80"/>
        <rect class="tile-blue" x="390" y="240" width="78" height="80"/>
        <rect class="tile-sand" x="468" y="240" width="78" height="80"/>
        <rect class="tile-green" x="546" y="240" width="78" height="80"/>
        <rect class="tile-blue" x="624" y="240" width="78" height="80"/>

        <rect class="tile-sand" x="0" y="320" width="78" height="80"/>
        <rect class="tile-blue" x="78" y="320" width="78" height="80"/>
        <rect class="tile-green" x="156" y="320" width="78" height="80"/>
        <rect class="tile-sand" x="234" y="320" width="78" height="80"/>
        <rect class="tile-green" x="312" y="320" width="78" height="80"/>
        <rect class="tile-sand" x="390" y="320" width="78" height="80"/>
        <rect class="tile-blue" x="468" y="320" width="78" height="80"/>
        <rect class="tile-green" x="546" y="320" width="78" height="80"/>
        <rect class="tile-sand" x="624" y="320" width="78" height="80"/>
      </g>
      <rect class="veil" x="0" y="0" width="700" height="400"/>
    </svg>
    <div class="identity">
      <h2 class="name">Lorra Vambeck</h2>
      <span class="divider"></span>
      <ul class="contacts">
        <li class="contact">
          <svg viewBox="0 0 14 14" aria-hidden="true"><circle cx="7" cy="7" r="5.5" fill="none" stroke="#b8913f" stroke-width="1.6"/></svg>
          @lra_vmbk
        </li>
        <li class="contact">
          <svg viewBox="0 0 14 14" aria-hidden="true"><rect x="1" y="3" width="12" height="8.5" fill="none" stroke="#b8913f" stroke-width="1.4"/><path d="M1 3.5 L7 8 L13 3.5" fill="none" stroke="#b8913f" stroke-width="1.4"/></svg>
          LorraVambeck@mailbox.example
        </li>
        <li class="contact">
          <svg viewBox="0 0 14 14" aria-hidden="true"><circle cx="7" cy="7" r="5.8" fill="none" stroke="#b8913f" stroke-width="1.3"/><ellipse cx="7" cy="7" rx="2.5" ry="5.8" fill="none" stroke="#b8913f" stroke-width="1.1"/><path d="M1.2 7 H12.8" stroke="#b8913f" stroke-width="1.1"/></svg>
          www.brightcoremotion.example
        </li>
      </ul>
    </div>
  </section>
</main>
</body>
</html>
```